General Graphic Chart and several template items to create

We need the following to be created for our company where we already have a logo set which we are not changing, but we are lacking all additional items that have a set graphic chart and templates to play with. The winner of this contest will be receiving requests on ongoing basis for graphic by us and some co-branded with our clients.

We need to have created the following in a templated setup where our staff can use the graphical layout and edit the content by themselves. The inspiration is the current logo of the company, but the whole needs to inspire "technology", "visual", "dynamic", "serious", "not to yellowish like in the logo":
1. Stationary
2. Website Banners (advertisement banners)
3. Offers sent out to B2B customers
4. General 1 pagers leaflets to put inside brochures
5. PPT presentation template
6. Tri-fold brochure
7. A mascot

This might sound a lot but it is an exercise over time for the winner with good reward.

Thanks

```html
<!DOCTYPE html>
<html lang="en">
<head>
<meta charset="utf-8">
<title>nexalink – Brand Stationery Board</title>
<link href="https://fonts.googleapis.com/css2?family=Montserrat:wght@400;500;600;700;800&family=Oswald:wght@500&display=swap" rel="stylesheet">
<style>
  :root{
    --board:#656565;
    --teal:#12b0ac;
    --teal-dark:#0d8f8c;
    --navy:#0c2f3f;
    --orange:#f5a51c;
    --paper:#ffffff;
    --panel-grey:#efefef;
    --ink:#0c2f3f;
    --photo-a:#3a2416;
    --photo-b:#c58a4e;
    --photo-c:#f3d7a8;
  }
  *{box-sizing:border-box;margin:0;padding:0}
  html,body{width:1200px;height:1200px;overflow:hidden;background:var(--board)}
  body{font-family:"Montserrat",sans-serif;color:var(--ink)}
  .board{position:relative;width:1200px;height:1200px;background:var(--board)}
  .sheet{position:absolute;background:var(--paper);overflow:hidden;box-shadow:1px 2px 3px rgba(0,0,0,.35)}
  .label{position:absolute;transform:translateX(-50%);font-family:"Oswald",sans-serif;font-weight:500;color:#fff;font-size:27px;letter-spacing:.2px;white-space:nowrap;line-height:1}
  .abs{position:absolute}
  .hexband{position:absolute;left:0;width:100%;background:linear-gradient(90deg,var(--navy) 0%,#14495a 30%,var(--teal-dark) 50%,#14495a 70%,var(--navy) 100%)}
  .photo{background:radial-gradient(circle at 45% 45%,var(--photo-c) 0%,var(--photo-b) 35%,var(--photo-a) 80%)}
  .brand{position:absolute;display:flex;align-items:center;font-family:"Montserrat",sans-serif;font-weight:600;color:var(--navy);white-space:nowrap;line-height:1}
  .brand .dot{display:inline-block;border-radius:50%;background:var(--orange);margin-right:.2em;width:.8em;height:.8em}
  .micro{font-size:4.3px;line-height:1.3;font-weight:500}
  .micro.j{text-align:justify}
  .feat{position:absolute;width:130px}
  .feat .head{display:flex;align-items:center;gap:4px;font-weight:700;font-size:8.5px;color:var(--navy)}
  .feat svg{width:15px;height:15px;stroke:var(--navy);fill:none;stroke-width:1.6}
  .feat .micro{margin-top:2px;color:var(--navy)}
  .w{color:#fff}
  .fold{position:absolute;top:0;height:100%;width:20px;background:linear-gradient(90deg,rgba(0,0,0,.08),rgba(0,0,0,0))}
  .hexicon{position:absolute;width:26px;height:28px}
  .contact{display:flex;align-items:center;gap:2px;font-size:4.6px;font-weight:600;color:#fff;white-space:nowrap}
  .contact i{display:inline-block;width:5px;height:5px;border:.8px solid #fff;border-radius:50%}
</style>
</head>
<body>
<svg width="0" height="0" style="position:absolute">
  <symbol id="i-people" viewBox="0 0 20 20"><circle cx="7" cy="6" r="3"/><circle cx="14" cy="7" r="2.5"/><path d="M2 17c0-4 2.5-6 5-6s5 2 5 6M11 12c1-1 2-1.5 3-1.5 2.2 0 4 1.8 4 5"/></symbol>
  <symbol id="i-bulb" viewBox="0 0 20 20"><circle cx="10" cy="8" r="5.5"/><path d="M8 14v3h4v-3M10.5 5l-2 3.5h3l-2 3"/></symbol>
  <symbol id="i-chart" viewBox="0 0 20 20"><path d="M2 2v16h16M4 14l4-5 3 3 6-7"/></symbol>
  <symbol id="i-plane" viewBox="0 0 20 20"><path d="M2 3l16 6-16 6 4-6zM6 9h12"/></symbol>
  <symbol id="i-search" viewBox="0 0 20 20"><circle cx="11" cy="8" r="5"/><path d="M7.5 11.5L3 17"/></symbol>
  <symbol id="i-rocket" viewBox="0 0 20 20"><path d="M4 16l3-1 8-8c1.5-1.5 2-4 2-4s-2.5.5-4 2l-8 8zM6 11l-3 0 2-3h3M9 14v3l3-2v-3"/></symbol>
  <symbol id="i-hex" viewBox="0 0 26 28"><polygon points="13,0 26,7 26,21 13,28 0,21 0,7"/></symbol>
</svg>

<main class="board">

  <!-- ============ TRI-FOLD BROCHURE: OUTSIDE ============ -->
  <section class="sheet trifold-outside" style="left:50px;top:38px;width:468px;height:332px">
    <div class="hexband" role="img" aria-label="Hexagon pattern strip" style="top:0;height:18px;width:310px"></div>
    <div class="abs" style="left:0;top:18px;width:310px;height:52px;background:var(--teal)"></div>
    <div class="abs photo" role="img" aria-label="Photo of hands joining puzzle pieces" style="left:310px;top:0;width:158px;height:332px"></div>
    <svg class="abs" style="left:0;top:0" width="468" height="120" viewBox="0 0 468 120">
      <path fill="var(--navy)" d="M195,70 Q198,112 245,112 L360,112 Q392,112 412,90 L468,38 L468,0 L310,0 L310,70 Z"/>
      <path fill="var(--teal)" d="M310,0 L468,0 L468,18 L405,76 Q390,90 362,90 L310,90 Z"/>
    </svg>
    <div class="abs w" style="left:318px;top:24px;font-size:17px;font-weight:600;line-height:1.1;text-align:center;width:140px">LOREM IPSUM<br>DOLOR SIT</div>

    <div class="abs w" style="left:28px;top:38px;font-size:17px;font-weight:800;letter-spacing:.3px">CONTENT</div>
    <div class="abs w" style="left:29px;top:56px;font-size:4.6px;font-weight:600">Lorem ipsum dolor sit amet</div>

    <div class="feat" style="left:20px;top:90px"><div class="head"><svg><use href="#i-people"/></svg>Lorem ipsum</div><p class="micro">Lorem ipsum dolor sit amet, consectetuer adipiscing elit, sed diam nonummy nibh euismod tincidunt ut laoreet dolore magna aliquam erat</p></div>
    <div class="feat" style="left:20px;top:137px"><div class="head"><svg><use href="#i-bulb"/></svg>Lorem ipsum</div><p class="micro">Lorem ipsum dolor sit amet, consectetuer adipiscing elit, sed diam nonummy nibh euismod tincidunt ut laoreet dolore magna aliquam erat</p></div>
    <div class="feat" style="left:20px;top:184px"><div class="head"><svg><use href="#i-chart"/></svg>Lorem ipsum</div><p class="micro">Lorem ipsum dolor sit amet, consectetuer adipiscing elit, sed diam nonummy nibh euismod tincidunt ut laoreet dolore magna aliquam erat</p></div>
    <div class="feat" style="left:20px;top:231px"><div class="head"><svg><use href="#i-plane"/></svg>Lorem ipsum</div><p class="micro">Lorem ipsum dolor sit amet, consectetuer adipiscing elit, sed diam nonummy nibh euismod tincidunt ut laoreet dolore magna aliquam erat</p></div>

    <div class="abs" style="left:0;top:292px;width:157px;height:40px;background:var(--teal)"></div>
    <svg class="hexicon" style="left:26px;top:280px" fill="var(--navy)"><use href="#i-hex"/></svg>
    <svg class="hexicon" style="left:66px;top:280px" fill="var(--navy)"><use href="#i-hex"/></svg>
    <svg class="hexicon" style="left:107px;top:280px" fill="var(--navy)"><use href="#i-hex"/></svg>
    <svg class="abs" style="left:32px;top:287px" width="14" height="14" fill="none" stroke="#fff" stroke-width="1.5"><use href="#i-people"/></svg>
    <svg class="abs" style="left:72px;top:287px" width="14" height="14" fill="none" stroke="#fff" stroke-width="1.5"><use href="#i-search"/></svg>
    <svg class="abs" style="left:113px;top:287px" width="14" height="14" fill="none" stroke="#fff" stroke-width="1.5"><use href="#i-rocket"/></svg>
    <div class="abs w" style="left:22px;top:312px;font-size:4.6px;font-weight:600;display:flex;gap:10px"><span>Lorem ipsum</span><span>Dolor sit amet</span><span>Consectetuer</span></div>

    <p class="abs micro w" style="left:178px;top:40px;width:125px;text-align:center;font-size:4.4px">Lorem ipsum dolor sit amet, consectetuer adipiscing elit, sed diam nonummy nibh euismod tincidunt ut laoreet dolore magna aliquam erat volutpat. Ut wisi enim ad minim veniam, quis nostrud exerci tation ullamcorper suscipit lobortis</p>

    <div class="brand" style="left:172px;top:178px;font-size:25px"><span class="dot"></span>nexalink</div>

    <div class="abs" style="left:157px;top:298px;width:153px;height:34px;background:var(--teal)"></div>
    <div class="abs" style="left:184px;top:304px;display:grid;grid-template-columns:auto auto;gap:4px 14px">
      <span class="contact"><i></i>001 234 5678</span><span class="contact"><i></i>Your e-mail here</span>
      <span class="contact"><i></i>Your website</span><span class="contact"><i></i>Your address here</span>
    </div>

    <div class="abs w" style="left:384px;top:234px;width:84px;height:52px;background:var(--navy);border-radius:14px 0 0 14px;padding:10px 0 0 10px;font-size:9.5px;font-weight:500;line-height:1.45">Lorem ipsum<br>dolor sit</div>
    <p class="abs micro w" style="left:390px;top:292px;width:72px;text-align:right;font-weight:600">Lorem ipsum dolor sit amet, consectetuer adipiscing elit, sed diam nonummy nibh ut laoreet dolore</p>
    <div class="fold" style="left:157px"></div>
  </section>

  <!-- ============ TRI-FOLD BROCHURE: INSIDE ============ -->
  <section class="sheet trifold-inside" style="left:50px;top:394px;width:468px;height:333px">
    <div class="abs" style="left:150px;top:22px;width:318px;height:44px;background:var(--teal)"></div>
    <svg class="abs" style="left:0;top:0" width="170" height="120" viewBox="0 0 170 120">
      <path fill="var(--navy)" d="M0,86 V48 C0,22 18,12 45,12 H120 C128,12 134,16 138,22 C120,34 95,48 60,54 C30,59 8,68 0,86 Z"/>
      <path fill="var(--teal)" d="M0,112 C4,80 28,66 70,66 H170 V22 H150 C130,22 118,34 100,44 C80,56 60,58 40,62 C20,66 5,80 0,90 Z"/>
    </svg>
    <div class="abs" style="left:14px;top:88px;font-size:31px;font-weight:500;color:var(--navy);line-height:1">01</div>
    <div class="abs" style="left:54px;top:93px;font-size:10.5px;font-weight:500;color:var(--navy);line-height:1.1">LOREM IPSUM<br>dolor sit amet</div>

    <div class="abs w" style="left:168px;top:28px;font-size:31px;font-weight:500;line-height:1">02</div>
    <div class="abs w" style="left:212px;top:33px;font-size:10px;font-weight:500;line-height:1.1">LOREM<br>IPSUM dolor</div>
    <div class="abs w" style="left:322px;top:28px;font-size:31px;font-weight:500;line-height:1">03</div>
    <div class="abs w" style="left:367px;top:33px;font-size:10px;font-weight:500;line-height:1.1">LOREM<br>IPSUM dolor</div>

    <div class="abs" style="left:14px;top:124px;width:128px;color:var(--navy)">
      <p class="micro j">Lorem ipsum dolor sit amet, consectetuer adipiscing elit, sed diam nonummy nibh euismod tincidunt ut laoreet dolore magna aliquam erat volutpat. Ut wisi enim ad minim</p>
      <p class="micro j" style="margin-top:5px;width:90px">Lorem ipsum dolor sit amet, consectetuer adipiscing elit, sed diam nonummy nibh euismod tincidunt ut laoreet dolore magna aliquam erat volutpat.</p>
      <p class="micro j" style="margin-top:5px">Lorem ipsum dolor sit amet, consectetuer adipiscing elit, sed diam nonummy nibh euismod tincidunt ut laoreet dolore magna aliquam erat volutpat. Ut wisi enim ad minim veniam, quis nostrud exerci tation ullamcorper suscipit lobortis nisl ut aliquip ex ea commodo consequat. Duis autem vel eum iriure dolor in hendrerit in vulputate velit esse molestie consequat, vel illum dolore eu feugiat nulla facilisis at vero eros et accumsan et iusto odio dignissim qui blandit praesent</p>
    </div>
    <svg class="hexicon" style="left:110px;top:164px" fill="var(--navy)"><use href="#i-hex"/></svg>
    <svg class="abs" style="left:116px;top:171px" width="14" height="14" fill="none" stroke="#fff" stroke-width="1.5"><use href="#i-plane"/></svg>

    <div class="abs" style="left:170px;top:75px;width:126px;color:var(--navy)">
      <p class="micro j">Lorem ipsum dolor sit amet, consectetuer adipiscing elit, sed diam nonummy nibh euismod tincidunt ut laoreet dolore magna aliquam erat volutpat. Ut wisi enim ad minim veniam, quis nostrud exerci tation ullamcorper suscipit lobortis nisl ut aliquip ex ea commodo consequat. Duis autem vel eum iriure dolor in hendrerit in vulputate velit esse molestie consequat, vel illum dolore eu feugiat nulla facilisis at vero eros et accumsan et iusto odio dignissim qui blandit praesent luptatum zzril delenit augue duis dolore te</p>
      <p class="micro j" style="margin:5px 0 0 37px">Lorem ipsum dolor sit amet, consectetuer adipiscing elit, sed diam nonummy nibh euismod tincidunt ut laoreet dolore magna aliquam erat volutpat. Ut</p>
      <p class="micro j" style="margin-top:4px">Lorem ipsum dolor sit amet, consectetuer adipiscing elit, sed diam nonummy nibh euismod tincidunt diam nonummy nibh ut v</p>
    </div>
    <svg class="hexicon" style="left:170px;top:180px" fill="var(--navy)"><use href="#i-hex"/></svg>
    <svg class="abs" style="left:176px;top:187px" width="14" height="14" fill="none" stroke="#fff" stroke-width="1.5"><use href="#i-chart"/></svg>

    <div class="abs" style="left:323px;top:75px;width:126px;color:var(--navy)">
      <p class="micro j">Lorem ipsum dolor sit amet, consectetuer adipiscing elit, sed diam nonummy nibh euismod tincidunt ut laoreet dolore magna aliquam erat volutpat. Ut wisi enim ad minim</p>
      <p class="micro j" style="margin-top:5px">Lorem ipsum dolor sit amet, consectetuer adipiscing elit, sed diam nonummy nibh euismod tincidunt ut laoreet dolore magna aliquam erat volutpat. Ut wisi enim ad minim veniam, quis nostrud exerci tation ullamcorper suscipit lobortis nisl ut aliquip ex ea commodo consequat. Duis autem vel eum iriure dolor in hendrerit in vulputate velit esse molestie consequat, vel illum dolore eu feugiat nulla facilisis at vero eros et accumsan et iusto odio dignissim qui blandit praesent</p>
      <p class="micro j" style="margin:5px 0 0 37px">Lorem ipsum dolor sit amet, consectetuer adipiscing elit, sed diam nonummy nibh euismod tincidunt ut laoreet dolore magna aliquam erat volutpat.</p>
    </div>
    <svg class="hexicon" style="left:323px;top:211px" fill="var(--navy)"><use href="#i-hex"/></svg>
    <svg class="abs" style="left:329px;top:218px" width="14" height="14" fill="none" stroke="#fff" stroke-width="1.5"><use href="#i-people"/></svg>

    <div class="fold" style="left:157px;width:26px"></div>
    <div class="fold" style="left:310px;width:26px"></div>
    <div class="hexband" role="img" aria-label="Hexagon pattern strip" style="top:302px;height:31px"></div>
  </section>
  <div class="label" style="left:283px;top:740px">TRI-FOLD BROCHURE</div>

  <!-- ============ B2B OFFER ============ -->
  <section class="sheet b2b-offer" style="left:50px;top:788px;width:468px;height:332px">
    <svg class="abs" style="left:0;top:0" width="468" height="332" viewBox="0 0 468 332">
      <path fill="var(--teal)" d="M0,95 C10,70 30,62 60,62 H335 L370,0 H0 Z"/>
      <polygon fill="var(--teal)" points="380,0 468,0 468,84 336,84"/>
      <polygon fill="var(--teal)" points="340,96 468,96 468,176 376,174"/>
      <polygon class="photo-hex" role="img" aria-label="Photo of hands joining puzzle pieces" fill="url(#photoGrad)" points="246,96 330,96 372,174 330,252 246,252 204,174"/>
      <polygon role="img" aria-label="Photo of a hand holding a puzzle piece" fill="url(#photoGrad2)" points="384,186 468,186 468,302 350,302 388,244"/>
      <defs>
        <radialGradient id="photoGrad" cx=".5" cy=".45" r=".6"><stop offset="0" stop-color="#f3d7a8"/><stop offset=".45" stop-color="#c58a4e"/><stop offset="1" stop-color="#3a2416"/></radialGradient>
        <radialGradient id="photoGrad2" cx=".3" cy=".3" r=".8"><stop offset="0" stop-color="#d9a56b"/><stop offset=".5" stop-color="#7a4a2a"/><stop offset="1" stop-color="#2a1a10"/></radialGradient>
      </defs>
    </svg>
    <div class="abs" style="left:46px;top:12px;font-size:31px;font-weight:800;color:var(--navy);letter-spacing:.5px;line-height:1">CONTENT</div>
    <div class="abs" style="left:57px;top:42px;font-size:9px;font-weight:500;color:var(--navy)">Lorem ipsum dolor sit amet</div>

    <div class="feat" style="left:58px;top:72px;width:125px"><div class="head"><svg><use href="#i-people"/></svg>Lorem ipsum</div><p class="micro">Lorem ipsum dolor sit amet, consectetuer adipiscing elit, sed diam nonummy nibh euismod tincidunt ut laoreet dolore magna aliquam erat</p></div>
    <div class="feat" style="left:58px;top:122px;width:125px"><div class="head"><svg><use href="#i-bulb"/></svg>Lorem ipsum</div><p class="micro">Lorem ipsum dolor sit amet, consectetuer adipiscing elit, sed diam nonummy nibh euismod tincidunt ut laoreet dolore magna aliquam erat</p></div>
    <div class="feat" style="left:58px;top:172px;width:125px"><div class="head"><svg><use href="#i-chart"/></svg>Lorem ipsum</div><p class="micro">Lorem ipsum dolor sit amet, consectetuer adipiscing elit, sed diam nonummy nibh euismod tincidunt ut laoreet dolore magna aliquam erat</p></div>
    <div class="feat" style="left:58px;top:219px;width:125px"><div class="head"><svg><use href="#i-plane"/></svg>Lorem ipsum</div><p class="micro">Lorem ipsum dolor sit amet, consectetuer adipiscing elit, sed diam nonummy nibh euismod tincidunt ut laoreet dolore magna aliquam erat</p></div>

    <div class="brand" style="left:50px;top:266px;font-size:24px"><span class="dot"></span>nexalink</div>
    <div class="hexband" role="img" aria-label="Hexagon pattern strip" style="top:302px;height:30px"></div>
  </section>
  <div class="label" style="left:286px;top:1140px">OFFERS SENT OUT TO B2B CUSTOMERS</div>

  <!-- ============ STATIONERY ============ -->
  <section class="sheet stationery" style="left:582px;top:38px;width:331px;height:468px">
    <div class="hexband" role="img" aria-label="Hexagon pattern strip" style="top:0;height:46px"></div>
    <div class="brand" style="left:215px;top:68px;font-size:17px"><span class="dot"></span>nexalink</div>
    <div class="abs" role="img" aria-label="Faint hexagon pattern" style="left:212px;top:120px;width:119px;height:200px;background:radial-gradient(ellipse at 60% 50%,#e6ecee 0%,#eef3f4 45%,rgba(255,255,255,0) 75%)"></div>
    <div class="hexband" role="img" aria-label="Hexagon pattern strip" style="top:414px;height:54px"></div>
  </section>
  <div class="label" style="left:745px;top:524px">STATIONARY</div>

  <!-- ============ LEAFLET ============ -->
  <section class="sheet leaflet" style="left:976px;top:38px;width:157px;height:332px">
    <svg class="abs" style="left:0;top:0" width="157" height="122" viewBox="0 0 157 122">
      <defs><radialGradient id="leafPhoto" cx=".55" cy=".45" r=".6"><stop offset="0" stop-color="#f3d7a8"/><stop offset=".45" stop-color="#c58a4e"/><stop offset="1" stop-color="#3a2416"/></radialGradient></defs>
      <polygon fill="var(--teal)" points="105,0 157,0 157,50 130,50"/>
      <polygon role="img" aria-label="Photo of hands joining puzzle pieces" fill="url(#leafPhoto)" points="30,0 100,0 124,40 100,80 30,80 8,40"/>
      <polygon role="img" aria-label="Photo of a hand holding a puzzle piece" fill="url(#leafPhoto)" points="128,58 157,58 157,122 95,122"/>
    </svg>
    <div class="brand" style="left:5px;top:92px;font-size:14px"><span class="dot"></span>nexalink</div>
    <div class="abs" style="left:0;top:122px;width:157px;height:30px;background:var(--teal)"></div>
    <div class="abs w" style="left:84px;top:128px;font-size:10.5px;font-weight:800">CONTENT</div>
    <div class="abs w" style="left:88px;top:141px;font-size:3.6px;font-weight:600">Lorem ipsum dolor sit amet</div>
    <div class="abs" style="left:12px;top:152px;width:66px;height:134px;background:var(--navy)"></div>
    <div class="abs w" style="left:16px;top:158px;width:58px">
      <p style="font-size:4.2px;font-weight:700">Lorem ipsum</p><p style="font-size:2.8px;line-height:1.3">Lorem ipsum dolor sit amet, consectetuer adipiscing elit, sed diam nonummy nibh euismod tincidunt</p>
      <p style="font-size:4.2px;font-weight:700;margin-top:18px">Lorem ipsum</p><p style="font-size:2.8px;line-height:1.3">Lorem ipsum dolor sit amet, consectetuer adipiscing elit, sed diam nonummy nibh euismod tincidunt</p>
      <p style="font-size:4.2px;font-weight:700;margin-top:18px">Lorem ipsum</p><p style="font-size:2.8px;line-height:1.3">Lorem ipsum dolor sit amet, consectetuer adipiscing elit, sed diam nonummy nibh euismod tincidunt</p>
      <p style="font-size:4.2px;font-weight:700;margin-top:18px">Lorem ipsum</p><p style="font-size:2.8px;line-height:1.3">Lorem ipsum dolor sit amet, consectetuer adipiscing elit, sed diam nonummy nibh euismod tincidunt</p>
    </div>
    <div class="abs" style="left:88px;top:178px;width:62px;color:var(--navy);font-size:2.9px;line-height:1.3;text-align:justify">
      <p>Lorem ipsum dolor sit amet, consectetuer adipiscing elit, sed diam nonummy nibh euismod tincidunt ut laoreet dolore magna aliquam erat volutpat. Ut wisi enim ad minim</p>
      <p style="margin-top:4px">Lorem ipsum dolor sit amet, consectetuer adipiscing elit, sed diam nonummy nibh euismod tincidunt ut laoreet dolore.</p>
      <p style="margin-top:4px">Lorem ipsum dolor sit amet, consectetuer adipiscing elit, sed diam nonummy nibh euismod tincidunt ut laoreet dolore magna aliquam erat volutpat. Ut wisi enim ad minim veniam, quis nostrud exerci tation ullamcorper suscipit lobortis nisl ut aliquip ex ea commodo consequat.</p>
      <p style="margin-top:4px">Lorem ipsum dolor sit amet, consectetuer adipiscing elit, sed diam nonummy nibh euismod tincidunt ut laoreet dolore magna.</p>
    </div>
    <div class="abs" style="left:0;top:286px;width:157px;height:6px;background:var(--teal)"></div>
    <div class="abs" style="left:32px;top:298px;display:grid;grid-template-columns:auto auto;gap:4px 10px">
      <span class="contact" style="color:var(--navy);font-size:3.6px"><i style="border-color:var(--navy)"></i>001 234 5678</span><span class="contact" style="color:var(--navy);font-size:3.6px"><i style="border-color:var(--navy)"></i>Your e-mail here</span>
      <span class="contact" style="color:var(--navy);font-size:3.6px"><i style="border-color:var(--navy)"></i>Your website</span><span class="contact" style="color:var(--navy);font-size:3.6px"><i style="border-color:var(--navy)"></i>Your address here</span>
    </div>
    <div class="hexband" role="img" aria-label="Hexagon pattern strip" style="top:320px;height:12px"></div>
  </section>
  <div class="label" style="left:1050px;top:384px">LEAFLET</div>

  <!-- ============ WEBSITE BANNERS ============ -->
  <section class="sheet banner-wide" style="left:582px;top:626px;width:405px;height:50px">
    <div class="abs" role="img" aria-label="Hexagon cluster accent" style="left:0;top:0;width:48px;height:50px;background:linear-gradient(135deg,var(--navy) 0%,var(--teal-dark) 45%,rgba(255,255,255,0) 60%)"></div>
    <div class="brand" style="left:52px;top:16px;font-size:19px"><span class="dot"></span>nexalink</div>
    <div class="abs" role="img" aria-label="Hexagon cluster accent" style="right:0;bottom:0;width:40px;height:50px;background:linear-gradient(315deg,var(--navy) 0%,var(--teal-dark) 40%,rgba(255,255,255,0) 60%)"></div>
  </section>
  <section class="sheet banner-square" style="left:1006px;top:626px;width:167px;height:140px">
    <div class="abs" role="img" aria-label="Hexagon cluster accent" style="left:0;top:0;width:60px;height:45px;background:linear-gradient(140deg,var(--navy) 0%,var(--teal-dark) 40%,rgba(255,255,255,0) 62%)"></div>
    <div class="brand" style="left:17px;top:110px;font-size:14px"><span class="dot"></span>nexalink</div>
    <div class="abs" role="img" aria-label="Hexagon cluster accent" style="right:0;bottom:0;width:45px;height:55px;background:linear-gradient(320deg,var(--navy) 0%,var(--teal-dark) 38%,rgba(255,255,255,0) 60%)"></div>
  </section>
  <div class="label" style="left:868px;top:700px">WEBSITE BANNERS</div>

  <!-- ============ MASCOT ============ -->
  <div class="abs mascot" role="img" aria-label="Mascot: friendly hexagon-headed robot in navy, teal and orange hovering on a blue thruster" style="left:566px;top:752px;width:214px;height:360px;border-radius:40px 40px 60px 60px;background:linear-gradient(180deg,#1b5a74 0%,var(--navy) 35%,#f5a51c 42%,#1f6880 50%,#113a4c 80%,rgba(90,140,220,.6) 100%)"></div>
  <div class="label" style="left:663px;top:1140px">A MASCOT</div>

  <!-- ============ LOGO PANEL ============ -->
  <section class="abs logo-panel" style="left:833px;top:1022px;width:367px;height:132px;background:var(--panel-grey)">
    <div class="brand" style="left:46px;top:40px;font-size:54px"><span class="dot" style="width:.7em;height:.7em"></span>nexalink</div>
  </section>

</main>
</body>
</html>
```